Design a new pricing menu

See here for full brief:

https://www.notavio.com/l/QpR7-XkTbWmLsN3Hv82FjdYcaEe4Rz9KoP2
Updates

Project Deadline Extended
Reason: We've had some requests to extend contest.

Industry/Entity Type

Pricing

```html
<!DOCTYPE html>
<html lang="en">
<head>
<meta charset="utf-8">
<title>Tanning Pricing Menu</title>
<link href="https://fonts.googleapis.com/css2?family=Fira+Sans:wght@200;300;400;500;600;700;800&display=swap" rel="stylesheet">
<style>
  :root {
    --navy: #3b4f68;
    --yellow: #fdc843;
    --ink: #222629;
    --muted: #4d5d72;
    --rule: #d9dbde;
    --rule-dark: #8a8e93;
    --panel: #5a6574;
    --panel-deep: #4e5866;
    --panel-text: #e4e7ec;
    --white: #ffffff;
  }
  * { box-sizing: border-box; margin: 0; padding: 0; }
  html, body { width: 848px; height: 1200px; overflow: hidden; background: var(--white); }
  body { position: relative; font-family: "Fira Sans", Arial, sans-serif; color: var(--ink); }

  /* Section titles */
  .section-title { position: absolute; display: flex; align-items: center; }
  .title-tag {
    background: var(--navy); color: var(--white);
    font-weight: 700; letter-spacing: -0.3px;
    display: flex; align-items: center; justify-content: center;
  }
  .title-count {
    background: var(--yellow); color: var(--navy); font-weight: 800;
    display: flex; align-items: center; justify-content: center;
  }
  .title-note { color: var(--muted); font-weight: 300; line-height: 0.95; }

  .uv-title { left: 317px; top: 55px; }
  .uv-title .title-tag { width: 153px; height: 38px; font-size: 28px; }
  .uv-title .title-count { width: 37px; height: 38px; font-size: 34px; margin-left: 6px; }
  .uv-title .title-note { font-size: 14px; margin-left: 6px; }

  .sunless-title { left: 315px; top: 801px; }
  .sunless-title .title-tag { width: 115px; height: 40px; font-size: 28px; }
  .sunless-title .title-note { font-size: 14px; margin-left: 5px; }

  /* Tables */
  table { position: absolute; border-collapse: collapse; table-layout: fixed; }
  th { font-weight: 400; text-align: left; vertical-align: middle; font-size: 9.5px; line-height: 1.25; padding: 0 10px; }
  th strong { font-weight: 600; }
  td { text-align: center; font-weight: 700; font-size: 12.5px; line-height: 1.2; }

  .uv-table { left: 107px; top: 125px; width: 700px; }
  .uv-table th { height: 33px; border-bottom: 1px solid var(--rule); }
  .uv-table td { border-bottom: 1px solid var(--rule); border-left: 1px solid var(--rule); }
  .uv-table .level-cell { border-left: none; position: relative; }
  .uv-table .th-level { padding: 0 0 0 6px; }
  .uv-table .th-level b { font-size: 8px; font-weight: 700; vertical-align: -7px; margin-right: 10px; }
  .uv-table th.best, .uv-table td.best { background: var(--yellow); border-left: 1px solid #e8b730; border-right: 1px solid #e8b730; }
  .uv-table th + th { border-left: 1px solid var(--rule); }
  .uv-table th.th-pick { border-left: none; padding-left: 4px; }
  .level-num {
    position: absolute; right: 109px; top: 50%; transform: translateY(-50%);
    font-weight: 200; font-size: 44px; white-space: nowrap; color: var(--ink);
  }

  /* All Access panel */
  .access-panel {
    position: absolute; left: 169px; top: 494px; width: 509px; height: 207px;
    border-radius: 5px; overflow: hidden;
    background: linear-gradient(135deg, #636e7c 0%, var(--panel) 45%, var(--panel-deep) 100%);
  }
  .access-panel .texture { position: absolute; inset: 0; }
  .access-title { position: absolute; left: 147px; top: 20px; display: flex; align-items: center; }
  .access-title .title-box {
    width: 144px; height: 38px; border: 2px solid var(--yellow); color: var(--yellow);
    font-weight: 800; font-size: 25px; display: flex; align-items: center; justify-content: center; letter-spacing: -0.3px;
  }
  .access-title .title-note { color: var(--yellow); font-size: 14px; margin-left: 7px; }
  .access-table { left: 0; top: 89px; width: 509px; }
  .access-table th { height: 33px; color: var(--panel-text); border-top: 1px solid var(--white); border-left: 1px solid var(--white); }
  .access-table th.blank { border-top: none; border-left: none; }
  .access-table td { height: 73px; color: var(--white); border-top: 1px solid var(--white); border-bottom: 1px solid #c7ccd3; border-left: 1px solid var(--white); }
  .access-table .row-label { text-align: left; font-weight: 400; font-size: 10px; line-height: 1.35; padding-left: 13px; color: var(--panel-text); border-left: none; }
  .access-table .best { background: var(--yellow); color: var(--ink); }

  .sunless-table { left: 94px; top: 879px; width: 700px; }
  .sunless-table th { height: 33px; border-bottom: 1px solid var(--rule-dark); }
  .sunless-table th + th { border-left: 1px solid var(--rule-dark); }
  .sunless-table td { border-bottom: 1px solid var(--rule-dark); border-left: 1px solid var(--rule-dark); vertical-align: top; padding-top: 18px; }
  .sunless-table tr.row-plus td { padding-top: 13px; }
  .sunless-table .row-label { text-align: left; font-weight: 400; font-size: 10px; border-left: none; padding-left: 10px; }
  .sunless-table .best { background: var(--yellow); }
  .sunless-table .detail { display: block; font-weight: 300; font-size: 12.5px; margin-top: 2px; }
  .sunless-table .light { font-weight: 300; }
</style>
</head>
<body>

<header class="section-title uv-title">
  <div class="title-tag">UV Tanning</div>
  <div class="title-count">5</div>
  <div class="title-note">Levels of<br>Award Winning<br>Equipment</div>
</header>

<table class="uv-table">
  <colgroup>
    <col style="width:135px"><col style="width:111px"><col style="width:97px"><col style="width:95px">
    <col style="width:70px"><col style="width:44px"><col style="width:74px"><col style="width:74px">
  </colgroup>
  <thead>
    <tr>
      <th class="th-level"><b>LEVEL</b><span style="display:inline-block;vertical-align:middle">Choose<br>your equipment:</span></th>
      <th class="best">Best Monthly Rate<br>When paid annually</th>
      <th>Monthly Auto-Pay<br><strong>Committment</strong></th>
      <th>Monthly Auto-Pay<br><strong>Flex</strong></th>
      <th>30 Day<br>Unlimited</th>
      <th style="padding:0 6px">Single<br>Visit</th>
      <th>Buy 5,<br>Get 2 FREE</th>
      <th>Buy 10,<br>Get 5 FREE</th>
    </tr>
  </thead>
  <tbody>
    <tr style="height:73px">
      <td class="level-cell"><span class="level-num">1</span></td>
      <td class="best">$24/month<br>($288)</td><td>$25.88</td><td>$28.88</td><td>$59</td><td>$9</td><td>$45</td><td>$90<br>($6 each)</td>
    </tr>
    <tr style="height:66px">
      <td class="level-cell"><span class="level-num">2-3</span></td>
      <td class="best">$24/month<br>($288)</td><td>$38.88</td><td>$48.88</td><td>$79</td><td>$14</td><td>$70</td><td>$140<br>($9.33 each)</td>
    </tr>
    <tr style="height:79px">
      <td class="level-cell"><span class="level-num">4</span></td>
      <td class="best">$24/month<br>($288)</td><td>$48.88</td><td>$58.88</td><td>$99</td><td>$18</td><td>$90</td><td>$180<br>($12 each)</td>
    </tr>
    <tr style="height:74px">
      <td class="level-cell"><span class="level-num" style="margin-top:6px">ALL 5</span></td>
      <td class="best">$24/month<br>($288)</td><td>$68.88</td><td>$88.88</td><td>$129</td><td>$28</td><td>$120</td><td>$240<br>($16 each)</td>
    </tr>
  </tbody>
</table>

<section class="access-panel">
  <div class="texture" role="img" aria-label="Soft faceted slate background texture"></div>
  <div class="access-title">
    <div class="title-box">All Access</div>
    <div class="title-note">Complete<br>Tanning &amp;<br>Skincare</div>
  </div>
  <table class="access-table">
    <colgroup>
      <col style="width:136px"><col style="width:111px"><col style="width:96px"><col style="width:98px"><col style="width:68px">
    </colgroup>
    <thead>
      <tr>
        <th class="blank"></th>
        <th class="best" style="color:var(--ink)">Best Monthly Rate<br>When paid annually</th>
        <th>Monthly Auto-Pay<br><strong>Committment</strong></th>
        <th>Monthly Auto-Pay<br><strong>Flex</strong></th>
        <th>30 Day<br>Unlimited</th>
      </tr>
    </thead>
    <tbody>
      <tr>
        <td class="row-label">Includes all UV,<br>Sunless &amp; Glow Seraph</td>
        <td class="best">$74/month<br>($888)</td>
        <td>$99</td><td>$199</td><td>$149</td>
      </tr>
    </tbody>
  </table>
</section>

<header class="section-title sunless-title">
  <div class="title-tag">Sunless</div>
  <div class="title-note">AeroMist Pro<br>Heated<br>Sunless</div>
</header>

<table class="sunless-table">
  <colgroup>
    <col style="width:136px"><col style="width:110px"><col style="width:90px"><col style="width:89px">
    <col style="width:78px"><col style="width:50px"><col style="width:80px"><col style="width:67px">
  </colgroup>
  <thead>
    <tr>
      <th>Choose<br>your equipment:</th>
      <th class="best">1 Session/month</th>
      <th>5 Session/month<br><strong>Committment</strong></th>
      <th>5 Session/month<br><strong>Flex</strong></th>
      <th style="text-align:center">30 Day<br>Unlimited</th>
      <th style="text-align:center;padding:0 4px">Single<br>Visit</th>
      <th>Buy 3,<br>Get 1 FREE</th>
      <th>Buy 5,<br>Get 2 FREE</th>
    </tr>
  </thead>
  <tbody>
    <tr style="height:73px">
      <td class="row-label">AeroMist Pro</td>
      <td class="best" style="padding-top:24px">$18.88</td>
      <td>$49.99<span class="detail">($9.99 each)</span></td>
      <td>$65<span class="detail">($13 each)</span></td>
      <td>$599<span class="detail">($49/month)</span></td>
      <td>$33</td>
      <td>$99</td>
      <td>$165<span class="detail">($22 each)</span></td>
    </tr>
    <tr class="row-plus" style="height:65px">
      <td class="row-label">AeroMist Pro+<br>Includes multi-session</td>
      <td class="best">$25</td>
      <td>$75<span class="detail">($15 each)</span></td>
      <td>$95<span class="detail">($13 each)</span></td>
      <td>$899<span class="detail">($75/month)</span></td>
      <td style="padding-left:0;padding-right:0">$38-$48<span class="detail">varies</span></td>
      <td>$135<span class="detail">(1st time- $99)</span></td>
      <td>$199<span class="detail">($28 each)</span></td>
    </tr>
  </tbody>
</table>

</body>
</html>
```